Brisk Hive 360 Postcard Design, Double-Sided

Please read carefully and see attached. Designers that do not follow these instructions will not be selected. Limit ONE design submission per artist. The ONE design submission shall show both the front and the back designs. Designs must comply with the attached dismensions accounting for the bleed area to prevent designs from being cut off during printing. The attached business card and door tag designs have already been created, printed and are in use. The postcard shall be similar in design to the attached business card and door tag. All of the information that you need is attached. The overall size is 4.12" x 6.12" for the front. The back is different, see attached and scale to match template. I would like the Veteran Owned Business logo added as well. It would also be nice to see my photo incorporated somehow. I like the yellow on the door tag. It helps build contrast and pops out. Again, one design submission per designer that shows both the front and the back.

Target Market(s)

Please read all instructions and see attached.

Industry/Entity Type

Requirements
Must have
• Please read all instructions and see attached.
Nice to have
Should not have

```html
<!DOCTYPE html>
<html lang="en">
<head>
<meta charset="utf-8">
<title>Brisk Hive 360 Handyman – Postcard Front and Back</title>
<link rel="stylesheet" href="https://fonts.googleapis.com/css2?family=Anton&family=Oswald:wght@300;400;500;600&display=swap">
<style>
  :root {
    --canvas: #9a9a9a;
    --ink: #2a2a2a;
    --ink-deep: #1f1f1f;
    --yellow: #f4ea1c;
    --white: #ffffff;
    --black: #111111;
    --muted: #d9d9d9;
  }
  * { box-sizing: border-box; margin: 0; padding: 0; }
  html, body { width: 1147px; height: 1200px; overflow: hidden; }
  body { background: var(--canvas); position: relative; font-family: "Oswald", sans-serif; }

  .postcard {
    position: absolute;
    left: 163px;
    width: 848px;
    height: 570px;
    background: var(--white);
    transform: scale(0.967);
    transform-origin: top left;
    overflow: hidden;
    box-shadow: 0 4px 14px rgba(0,0,0,0.18);
  }
  .postcard--front { top: 30px; }
  .postcard--back { top: 617px; }

  /* Front */
  .front-dark { position: absolute; left: 0; top: 0; width: 848px; height: 384px; background: var(--ink); }
  .front-band { position: absolute; left: 0; top: 384px; width: 848px; height: 16px; background: var(--yellow); }

  .title { position: absolute; font-family: "Anton", sans-serif; text-transform: uppercase; line-height: 1; }
  .title__line { display: block; color: var(--yellow); }
  .title__rule { display: block; background: var(--yellow); height: 3px; }
  .title__sub { display: block; color: var(--white); }

  .front .title { left: 48px; top: 40px; }
  .front .title__line { font-size: 66px; letter-spacing: -0.5px; }
  .front .title__line + .title__line { margin-top: 6px; }
  .front .title__rule { width: 240px; margin-top: 8px; }
  .front .title__sub { font-size: 50px; margin-top: 6px; }

  .brand-mark { position: absolute; display: flex; align-items: center; justify-content: center; border-radius: 50%; border: 4px solid var(--white); }
  .brand-mark__name { font-family: "Anton", sans-serif; color: var(--white); text-transform: uppercase; text-align: center; line-height: 1.05; }
  .front .brand-mark { left: 328px; top: 42px; width: 210px; height: 210px; }
  .front .brand-mark__name { font-size: 30px; }

  .owner { position: absolute; left: 560px; top: 44px; width: 210px; text-align: center; }
  .owner__name { font-family: "Anton", sans-serif; color: var(--yellow); font-size: 26px; letter-spacing: 0.3px; line-height: 1; }
  .owner__role { font-family: "Oswald", sans-serif; font-weight: 600; color: var(--white); font-size: 12px; text-transform: uppercase; margin-top: 2px; }

  .placeholder { position: absolute; }
  .owner-photo { left: 585px; top: 92px; width: 183px; height: 210px; background: linear-gradient(180deg, #4a4a4a 0%, #8d8f92 55%, #b9bbbe 100%); }
  .photo-strip { top: 302px; height: 142px; border: 4px solid var(--white); box-shadow: 0 3px 8px rgba(0,0,0,0.3); }
  .photo-strip--doorbell { left: 52px; width: 242px; background: linear-gradient(90deg, #7a746d 0%, #9e9b97 50%, #d6d9dc 100%); }
  .photo-strip--hardware { left: 292px; top: 286px; width: 262px; height: 174px; border-color: var(--yellow); background: linear-gradient(135deg, #e6e8ec 0%, #cfd3d9 100%); z-index: 2; }
  .photo-strip--network { left: 552px; width: 240px; background: radial-gradient(circle at 45% 55%, #39b6e6 0%, #1c5fa0 45%, #0b1d3d 100%); }

  .contact-row { position: absolute; left: 0; top: 497px; width: 848px; height: 24px; font-family: "Oswald", sans-serif; font-weight: 500; font-size: 15.5px; color: var(--black); }
  .contact-row .contact { position: absolute; top: 0; display: flex; align-items: center; gap: 8px; white-space: nowrap; height: 24px; }
  .contact-row .divider { position: absolute; top: -4px; width: 1px; height: 32px; background: var(--black); }
  .icon { width: 18px; height: 18px; flex: none; }

  .badge { position: absolute; border-radius: 50%; background: #c62d36; border: 5px solid #1f3d7a; }
  .front .badge { left: 731px; top: 467px; width: 84px; height: 84px; }

  /* Back */
  .back-dark { position: absolute; left: 0; top: 0; width: 480px; height: 425px; background: var(--ink); }
  .back .title { left: 30px; top: 30px; }
  .back .title__line { font-size: 50px; }
  .back .title__rule { width: 297px; margin-top: 4px; }
  .back .title__sub { font-size: 40px; margin-top: 4px; }
  .back .brand-mark { left: 352px; top: 32px; width: 104px; height: 104px; border-width: 3px; }
  .back .brand-mark__name { font-size: 15px; }

  .list-block { position: absolute; color: var(--white); }
  .list-block__heading { font-family: "Anton", sans-serif; color: var(--yellow); font-size: 28px; text-transform: uppercase; line-height: 1; }
  .list-block__lead { font-size: 16px; font-weight: 300; margin-top: 4px; }
  .list-block ul { list-style: none; margin-top: 8px; }
  .list-block li { position: absolute; font-size: 16.5px; font-weight: 300; line-height: 1; padding-left: 17px; white-space: nowrap; }
  .list-block li::before { content: ""; position: absolute; left: 0; top: 6px; width: 7px; height: 7px; border-radius: 50%; background: var(--yellow); }
  .services { left: 30px; top: 178px; }
  .benefits { left: 287px; top: 178px; }
  .back-divider { position: absolute; left: 248px; top: 219px; width: 2px; height: 173px; background: var(--yellow); }

  .contact-list { position: absolute; left: 30px; top: 444px; list-style: none; font-family: "Oswald", sans-serif; font-weight: 500; font-size: 13.5px; color: var(--black); }
  .contact-list li { display: flex; align-items: center; gap: 9px; height: 25.5px; }
  .contact-list .icon { width: 15px; height: 15px; }

  .stamp-box { position: absolute; left: 680px; top: 40px; width: 129px; height: 128px; border: 2px solid var(--black); }
</style>
</head>
<body>

<section class="postcard postcard--front front" aria-label="Postcard front">
  <div class="front-dark"></div>
  <div class="front-band"></div>

  <h1 class="title">
    <span class="title__line">Brisk</span>
    <span class="title__line">Hive 360</span>
    <span class="title__rule"></span>
    <span class="title__sub">Handyman</span>
  </h1>

  <div class="brand-mark"><span class="brand-mark__name">Brisk<br>Hive 360</span></div>

  <div class="owner">
    <p class="owner__name">DANA R. WHITLOW</p>
    <p class="owner__role">Owner &amp; Handyman</p>
  </div>

  <div class="placeholder owner-photo" role="img" aria-label="Portrait photo of the owner in a grey uniform polo shirt"></div>

  <div class="placeholder photo-strip photo-strip--doorbell" role="img" aria-label="Photo of a video doorbell mounted beside a stone wall"></div>
  <div class="placeholder photo-strip photo-strip--hardware" role="img" aria-label="Photo of brass picture-hanging hooks and nails"></div>
  <div class="placeholder photo-strip photo-strip--network" role="img" aria-label="Illustration of a wifi router with connected devices"></div>

  <div class="contact-row">
    <span class="contact" style="left:28px">
      <svg class="icon" viewBox="0 0 20 20" aria-hidden="true"><circle cx="10" cy="10" r="10" fill="#111"/><path d="M6.5 5.2l2 0.3 0.8 2.4-1.3 1c0.7 1.4 1.8 2.5 3.1 3.1l1-1.3 2.4 0.8 0.3 2c-0.4 0.9-1.4 1.3-2.4 1.1-3.5-0.8-6-3.4-6.8-6.8-0.2-1 0.2-2 1.1-2.4z" fill="#fff"/></svg>
      (555) 014-2290
    </span>
    <span class="divider" style="left:161px"></span>
    <span class="contact" style="left:178px">
      <svg class="icon" viewBox="0 0 20 20" aria-hidden="true"><circle cx="10" cy="10" r="10" fill="#111"/><path d="M10 4.5a3.8 3.8 0 0 0-3.8 3.8c0 2.8 3.8 7 3.8 7s3.8-4.2 3.8-7A3.8 3.8 0 0 0 10 4.5z" fill="#fff"/><circle cx="10" cy="8.3" r="1.5" fill="#111"/></svg>
      Bayview, Florida
    </span>
    <span class="divider" style="left:338px"></span>
    <span class="contact" style="left:358px">
      <svg class="icon" viewBox="0 0 20 20" aria-hidden="true"><circle cx="10" cy="10" r="10" fill="#111"/><rect x="5" y="6.5" width="10" height="7" fill="#fff"/><path d="M5 6.5l5 4 5-4" fill="none" stroke="#111" stroke-width="1"/></svg>
      Service@BriskHive360.com
    </span>
    <span class="divider" style="left:565px"></span>
    <span class="contact" style="left:583px">
      <svg class="icon" viewBox="0 0 20 20" aria-hidden="true"><circle cx="10" cy="10" r="10" fill="#111"/><circle cx="10" cy="10" r="5.5" fill="none" stroke="#fff" stroke-width="1.2"/><ellipse cx="10" cy="10" rx="2.3" ry="5.5" fill="none" stroke="#fff" stroke-width="1.1"/><path d="M4.5 10h11" stroke="#fff" stroke-width="1.1"/></svg>
      BriskHive360.com
    </span>
  </div>

  <div class="badge" aria-hidden="true"></div>
</section>

<section class="postcard postcard--back back" aria-label="Postcard back">
  <div class="back-dark"></div>

  <h2 class="title">
    <span class="title__line">Brisk Hive 360</span>
    <span class="title__rule"></span>
    <span class="title__sub">Handyman</span>
  </h2>

  <div class="brand-mark"><span class="brand-mark__name">Brisk<br>Hive 360</span></div>

  <div class="list-block services">
    <h3 class="list-block__heading">Services</h3>
    <ul>
      <li style="top:38px">Assembly</li>
      <li style="top:62px">Small Repairs</li>
      <li style="top:86px">Wifi / Router Setup</li>
      <li style="top:110px">Fabrication</li>
      <li style="top:134px">Hanging Items</li>
      <li style="top:158px">Wireless Devise Setup</li>
      <li style="top:182px">Odd Jobs</li>
    </ul>
  </div>

  <div class="back-divider"></div>

  <div class="list-block benefits">
    <h3 class="list-block__heading">Benefits</h3>
    <p class="list-block__lead">of using our services</p>
    <ul>
      <li style="top:73px">Fast Response</li>
      <li style="top:100px">High Quality</li>
      <li style="top:128px">Fair Pricing</li>
      <li style="top:155px">Veteran Owned</li>
    </ul>
  </div>

  <ul class="contact-list">
    <li>
      <svg class="icon" viewBox="0 0 20 20" aria-hidden="true"><circle cx="10" cy="10" r="10" fill="#111"/><path d="M6.5 5.2l2 0.3 0.8 2.4-1.3 1c0.7 1.4 1.8 2.5 3.1 3.1l1-1.3 2.4 0.8 0.3 2c-0.4 0.9-1.4 1.3-2.4 1.1-3.5-0.8-6-3.4-6.8-6.8-0.2-1 0.2-2 1.1-2.4z" fill="#fff"/></svg>
      (555) 014-2290
    </li>
    <li>
      <svg class="icon" viewBox="0 0 20 20" aria-hidden="true"><circle cx="10" cy="10" r="10" fill="#111"/><path d="M10 4.5a3.8 3.8 0 0 0-3.8 3.8c0 2.8 3.8 7 3.8 7s3.8-4.2 3.8-7A3.8 3.8 0 0 0 10 4.5z" fill="#fff"/><circle cx="10" cy="8.3" r="1.5" fill="#111"/></svg>
      Bayview, Florida
    </li>
    <li>
      <svg class="icon" viewBox="0 0 20 20" aria-hidden="true"><circle cx="10" cy="10" r="10" fill="#111"/><rect x="5" y="6.5" width="10" height="7" fill="#fff"/><path d="M5 6.5l5 4 5-4" fill="none" stroke="#111" stroke-width="1"/></svg>
      Service@BriskHive360.com
    </li>
    <li>
      <svg class="icon" viewBox="0 0 20 20" aria-hidden="true"><circle cx="10" cy="10" r="10" fill="#111"/><circle cx="10" cy="10" r="5.5" fill="none" stroke="#fff" stroke-width="1.2"/><ellipse cx="10" cy="10" rx="2.3" ry="5.5" fill="none" stroke="#fff" stroke-width="1.1"/><path d="M4.5 10h11" stroke="#fff" stroke-width="1.1"/></svg>
      BriskHive360.com
    </li>
  </ul>

  <div class="stamp-box" aria-label="Stamp area"></div>
</section>

</body>
</html>
```